Simple templates for management consulting firm

Vireo Associates is a management consulting firm based in the DC area. We have all the basic templates but would like to tweak them so they look consistent.

Check us out at www.vireoassociates-example.com

For this project we would like to get
a tweaked powerpoint template (header should be up)
a letter template for letters
a fax template

Current templates and our logo are attached.
Updates

We just increased the budget of this project.

We got questions about the project. Here are our thoughts on this one:

Please include the logo into the fax template. If you find improvements in the layout then feel free to make those. Let's not overthink this too much. Keep it simple :)

We like The powerpoint concept as is. The slide titles are for some reasons on the bottom. It seems to irritate some folks. If you can switch the slide titles to the top, keep the look and feel of the slides and work in the logo then that would be fantastic.

The letter head should include the following

Vireo Associates, LLC Box 5827, Millbrook, VA 20147 Phone 703 518-9461, Fax 703 286 7135, www.vireoassociates-example.com and the logo.

Again, let's keep it simple.

Thank you for considering this project.

We just realize that we are not necessarily inisting to use the red in the slides.
Any approach that would work with the logo will be considered.

Thanks for your creativity.

Target Market(s)

tech companies, Pinnacle 400, venture capitalists

Industry/Entity Type

Management Consulting

Requirements
Must have
• Keep it simple please

```html
<!DOCTYPE html>
<html lang="en">
<head>
<meta charset="utf-8">
<title>Vireo Associates Letterhead</title>
<link href="https://fonts.googleapis.com/css2?family=Cinzel:wght@400&family=PT+Sans:wght@400&display=swap" rel="stylesheet">
<style>
  :root {
    --brand-red: #660000;
    --brand-red-line: #7a1010;
    --paper: #fdfdfd;
    --silver: #d4d4d4;
    --gold: #d9a93c;
    --ink: #1a1a1a;
  }
  html, body {
    margin: 0;
    padding: 0;
    overflow: hidden;
    background: #ffffff;
  }
  .letterhead {
    position: relative;
    width: 928px;
    height: 1200px;
    background: var(--paper);
    overflow: hidden;
  }
  .header-band {
    position: absolute;
    left: 54px;
    top: 54px;
    width: 826px;
    height: 113px;
    background: var(--brand-red);
    border-top: 2px solid var(--brand-red-line);
    box-sizing: border-box;
  }
  .header-band::before {
    content: "";
    position: absolute;
    left: 0;
    right: 0;
    top: 10px;
    height: 1px;
    background: var(--brand-red-line);
  }
  .brand {
    position: absolute;
    left: 8px;
    top: 18px;
    display: flex;
    align-items: center;
    gap: 14px;
  }
  .brand-mark {
    width: 78px;
    height: 78px;
    border-radius: 50%;
    background: var(--gold);
  }
  .brand-name {
    font-family: "Cinzel", serif;
    font-weight: 400;
    font-size: 40px;
    letter-spacing: 1px;
    color: var(--silver);
    line-height: 1;
  }
  .footer-rule {
    position: absolute;
    left: 46px;
    top: 1093px;
    width: 841px;
    height: 10px;
    background: var(--brand-red);
  }
  .footer-contact {
    position: absolute;
    left: 0;
    top: 1107px;
    width: 928px;
    margin: 0;
    text-align: center;
    font-family: "PT Sans", sans-serif;
    font-size: 12.5px;
    line-height: 16px;
    color: var(--ink);
  }
</style>
</head>
<body>
  <div class="letterhead">
    <header class="header-band">
      <div class="brand">
        <div class="brand-mark"></div>
        <div class="brand-name">Vireo Associates</div>
      </div>
    </header>

    <div class="footer-rule"></div>
    <p class="footer-contact">
      Vireo Associates, LLC Box 5827 Millbrook, VA 20147 &bull; Phone 703 518-9461 Fax 703 286 7135<br>
      www.vireoassociates-example.com
    </p>
  </div>
</body>
</html>
```